Packaging for baby product company

We require a packaging design for our new baby brush kit we are launching.

I have attached the logo pernwix.pdf (when winner is chosen we can replace with .ai file) for our brand and images of the items inside the packaging. The packaging is two pieces as per the ref1 image. it shows the bottom part of the packaging so please take into consideration for design that we need lid and bottom.

the design should communicate comfort and reliability to our audience of parents.

New parents

Baby

```html
<!DOCTYPE html>
<html lang="en">
<head>
<meta charset="utf-8">
<title>Pernwix Baby Brush Kit – Packaging</title>
<link href="https://fonts.googleapis.com/css2?family=Amatic+SC:wght@400;700&display=swap" rel="stylesheet">
<style>
  :root {
    --paper: #ffffff;
    --pink-wash: #fde3e6;
    --blue-wash: #dcebfb;
    --leaf: rgba(190, 215, 180, 0.35);
    --purple: #8c62b0;
    --orange: #f7941d;
    --green: #5fcc1f;
    --pink: #f06fa8;
    --wood-light: #e9a767;
    --wood-dark: #c8743a;
    --bristle: #e9d5a8;
  }
  * { margin: 0; padding: 0; box-sizing: border-box; }
  html, body { width: 1200px; height: 1200px; overflow: hidden; background: var(--paper); }
  body { position: relative; font-family: "Amatic SC", "Arial Narrow", sans-serif; }

  .panel { position: absolute; overflow: hidden; }
  .panel--lid {
    left: 35px; top: 30px; width: 579px; height: 1128px;
    background: linear-gradient(180deg, var(--pink-wash) 0%, #fff6f5 45%, var(--blue-wash) 100%);
  }
  .panel--side {
    left: 753px; top: 28px; width: 413px; height: 1138px;
    background: linear-gradient(90deg, var(--blue-wash) 0%, #f7f9fd 55%, var(--pink-wash) 100%);
  }
  .foliage {
    position: absolute; inset: 0;
    background:
      radial-gradient(ellipse 45% 30% at 40% 15%, var(--leaf), transparent 70%),
      radial-gradient(ellipse 40% 25% at 70% 90%, var(--leaf), transparent 70%),
      radial-gradient(ellipse 35% 25% at 15% 60%, var(--leaf), transparent 70%);
  }
  .sun {
    position: absolute; right: -40px; bottom: 110px; width: 150px; height: 150px;
    border-radius: 50%; background: rgba(250, 190, 190, 0.45);
  }

  .item { position: absolute; }
  .brush {
    border-radius: 50% 50% 40% 40% / 30% 30% 12% 12%;
    background: linear-gradient(180deg, var(--bristle) 0%, var(--bristle) 44%, var(--wood-light) 46%, var(--wood-dark) 100%);
  }
  .brush--paddle { background: linear-gradient(180deg, #c9a06a 0%, #b98850 44%, var(--wood-light) 46%, var(--wood-dark) 100%); }
  .comb {
    border-radius: 10px 10px 30px 30px;
    background: linear-gradient(90deg, var(--bristle) 0%, var(--bristle) 45%, var(--wood-light) 47%, var(--wood-dark) 100%);
  }

  .brand {
    position: absolute; color: var(--orange); font-weight: 700; line-height: 1;
    display: flex; align-items: center; gap: 14px;
  }
  .brand__dot { width: 22px; height: 22px; border-radius: 50%; background: var(--orange); }

  .lid-title {
    position: absolute; left: 0; width: 100%; top: 352px; text-align: center;
    color: var(--purple); font-weight: 700; font-size: 118px; line-height: 1; letter-spacing: 2px;
  }
  .lid-copy {
    position: absolute; left: 67px; top: 868px; width: 470px;
    color: var(--purple); font-size: 27px; line-height: 27px; font-weight: 700;
    text-align: justify; text-transform: uppercase;
  }

  .vtext {
    position: absolute; writing-mode: vertical-rl; font-weight: 700;
    line-height: 1; white-space: nowrap; text-transform: uppercase;
  }
  .vtext--name { color: var(--purple); font-size: 40px; }
  .vtext--use { color: var(--orange); font-size: 40px; }
  .side-title { font-size: 104px; letter-spacing: 2px; }
  .side-title .w1 { color: var(--green); }
  .side-title .w2 { color: var(--pink); }
  .side-title .w3 { color: var(--orange); }
</style>
</head>
<body>

<section class="panel panel--lid">
  <div class="foliage" role="img" aria-label="Soft pastel leaf illustration background"></div>

  <div class="brand" style="left:118px; top:170px; font-size:96px;">
    <span class="brand__dot"></span><span>Pernwix</span>
  </div>

  <h1 class="lid-title">Baby Brush Kit</h1>

  <div class="item brush brush--paddle" style="left:121px; top:462px; width:100px; height:352px;" role="img" aria-label="Wooden paddle brush with wooden pins"></div>
  <div class="item comb" style="left:255px; top:590px; width:74px; height:224px;" role="img" aria-label="Wooden fine-tooth comb"></div>
  <div class="item brush" style="left:363px; top:454px; width:98px; height:360px;" role="img" aria-label="Wooden soft natural-bristle scalp brush"></div>

  <p class="lid-copy">Babies love this brush as it massages and stimulates their tender scalp with the natural bristles; using this baby hair brush for their hair everyday before bed and in the morning helps your baby be calm and relaxed</p>
</section>

<section class="panel panel--side">
  <div class="foliage" role="img" aria-label="Soft pastel leaf illustration background"></div>
  <div class="sun"></div>

  <div class="item brush" style="left:63px; top:100px; width:68px; height:248px;" role="img" aria-label="Soft scalp brush"></div>
  <div class="vtext vtext--name" style="left:139px; top:144px;">Soft scalp brush</div>
  <div class="vtext vtext--use" style="left:23px; top:176px;">For baby</div>

  <div class="item comb" style="left:71px; top:488px; width:48px; height:156px;" role="img" aria-label="Wooden comb"></div>
  <div class="vtext vtext--name" style="left:135px; top:464px;">Quality wooden comb</div>
  <div class="vtext vtext--use" style="left:27px; top:492px;">For longer hair</div>

  <div class="item brush brush--paddle" style="left:59px; top:820px; width:68px; height:244px;" role="img" aria-label="Paddle brush with wooden pins"></div>
  <div class="vtext vtext--name" style="left:139px; top:852px;">Hard bristle comb</div>
  <div class="vtext vtext--use" style="left:19px; top:848px;">For the toddler age</div>

  <div class="vtext side-title" style="left:201px; top:370px;">
    <span class="w1">Baby</span> <span class="w2">Brush</span> <span class="w3">Kit</span>
  </div>

  <div class="vtext brand" style="left:310px; top:440px; font-size:92px;">
    <span class="brand__dot"></span><span>Pernwix</span>
  </div>
</section>

</body>
</html>
```